PELDRAX Business Cards

We require a business card for our company that provides IT consulting services. We already have a logo that needs to be used on the card. We want a clean professional looking design that incorporates our colours. Our main focus is providing managed services to business, which involves us looking after all of their IT requirements including managing servers/networks, projects, and procurement.

Industry/Entity Type

Information Technology

Requirements
Must have
• our logo, contact information, name, title, phone numbers

```html
<!DOCTYPE html>
<html lang="en">
<head>
<meta charset="utf-8">
<title>PELDRAX Business Cards</title>
<link href="https://fonts.googleapis.com/css2?family=Lato:wght@300;400;700;900&display=swap" rel="stylesheet">
<style>
  :root{
    --brand-blue:#0093cd;
    --ink:#1e1e1e;
    --white:#ffffff;
    --bg-light:#d7d8da;
    --bg-dark:#8b8c90;
    --edge:#2a2a2a;
  }
  *{margin:0;padding:0;box-sizing:border-box}
  html,body{width:1200px;height:1137px;overflow:hidden}
  body{
    position:relative;
    background:linear-gradient(90deg,var(--bg-light) 0%,var(--bg-dark) 100%);
    font-family:"Lato",Arial,sans-serif;
    color:var(--ink);
  }
  .card{position:absolute;width:794px;height:454px;border-radius:34px;overflow:hidden}
  .card-front{left:322px;top:77px;background:var(--white);border:1px solid var(--edge)}
  .card-back{left:58px;top:610px;background:var(--brand-blue)}

  .name-marker{position:absolute;left:0;top:76px;width:17px;height:50px;background:var(--brand-blue)}
  .holder-name{position:absolute;left:36px;top:78px;font-size:21px;font-weight:700;color:var(--brand-blue);letter-spacing:.3px}
  .holder-title{position:absolute;left:36px;top:104px;font-size:19px;font-weight:300;color:var(--ink)}

  .brand{position:absolute;right:38px;top:70px;display:flex;align-items:center;gap:14px}
  .brand-dot{width:58px;height:58px;border-radius:50%;background:var(--brand-blue)}
  .brand-name{font-size:60px;font-weight:700;color:var(--brand-blue);letter-spacing:2px;line-height:1}

  .contacts{position:absolute;left:36px;top:222px;list-style:none}
  .contacts li{display:flex;align-items:center;height:31.5px;font-size:20px;font-weight:400}
  .contacts svg{width:15px;height:15px;margin-right:8px;flex:none}

  .footer-band{position:absolute;left:0;bottom:0;width:794px;height:62px}
  .address{position:absolute;left:36px;bottom:33px;display:flex;align-items:center;color:var(--white);font-size:18px}
  .address svg{width:15px;height:15px;margin-right:8px}

  .back-brand{position:absolute;left:0;right:0;top:150px;text-align:center;font-size:96px;font-weight:700;color:var(--white);letter-spacing:4px}
  .back-web{position:absolute;left:0;right:0;top:387px;text-align:center;font-size:22px;font-weight:400;color:var(--white);letter-spacing:4.5px}
</style>
</head>
<body>

<section class="card card-front">
  <div class="name-marker"></div>
  <div class="holder-name">MARCUS DELFORD</div>
  <div class="holder-title">PRESIDENT</div>

  <div class="brand">
    <span class="brand-dot"></span>
    <span class="brand-name">PELDRAX</span>
  </div>

  <ul class="contacts">
    <li>
      <svg viewBox="0 0 16 16" fill="none" stroke="var(--brand-blue)" stroke-width="1.4"><circle cx="8" cy="8" r="7"/><path d="M6 4.5l1.3 2-1 1a5 5 0 0 0 2.2 2.2l1-1 2 1.3-.8 1.4c-3 0-5.6-2.6-5.6-5.6z" fill="var(--brand-blue)" stroke="none"/></svg>
      012-345-6789
    </li>
    <li>
      <svg viewBox="0 0 16 16" fill="none" stroke="var(--brand-blue)" stroke-width="1.5"><rect x="4" y="1" width="8" height="14" rx="1.5"/><line x1="7" y1="12.5" x2="9" y2="12.5"/></svg>
      012-345-6789
    </li>
    <li>
      <svg viewBox="0 0 16 16"><path d="M1 6l7-4 7 4v8H1z" fill="var(--brand-blue)"/><path d="M1 6l7 4.5L15 6" fill="none" stroke="var(--white)" stroke-width="1.2"/></svg>
      info@peldrax.com
    </li>
    <li>
      <svg viewBox="0 0 16 16" fill="none" stroke="var(--brand-blue)" stroke-width="1.2"><circle cx="8" cy="8" r="7"/><ellipse cx="8" cy="8" rx="3" ry="7"/><line x1="1" y1="8" x2="15" y2="8"/><line x1="2" y1="4.5" x2="14" y2="4.5"/><line x1="2" y1="11.5" x2="14" y2="11.5"/></svg>
      www.peldrax.com
    </li>
  </ul>

  <svg class="footer-band" viewBox="0 0 794 62" preserveAspectRatio="none">
    <rect x="0" y="0" width="794" height="62" fill="var(--brand-blue)"/>
    <path d="M0 0 H538 C512 2 514 32 488 32 H0 Z" fill="#000"/>
  </svg>
  <div class="address">
    <svg viewBox="0 0 16 16" fill="none" stroke="var(--white)" stroke-width="1.5"><circle cx="8" cy="8" r="7"/><path d="M8 12.5s-3-3-3-5.2a3 3 0 0 1 6 0c0 2.2-3 5.2-3 5.2z"/><circle cx="8" cy="7.2" r="1" fill="var(--white)"/></svg>
    123, Street Name, City Name, Zipcode - 01234
  </div>
</section>

<section class="card card-back">
  <div class="back-brand">PELDRAX</div>
  <div class="back-web">www.peldrax.com</div>
</section>

</body>
</html>
```